Virtual background for e-learning webinar presenter

I would like to create a virtual background for our webinar presentations. I would like it to have a background of a modern surgical suite with our logo. The surgical suite that I have included is free for public use.

Our company is called pawkenri.com.

Target Market(s)

Primary care veterinarians

Font styles to use
Sans Serif

Requirements
Must have
• Must look professional. We are promoting a e-learning platform for veterinarians. Must look like an elite modern professional educational platform.
Nice to have
• Modern surgical suite. Match existing logo which has been provided.
Should not have
• Other than our logo, no cutesy dogs, cats or puppies

```html
<!DOCTYPE html>
<html lang="en">
<head>
<meta charset="utf-8">
<title>Virtual background for e-learning webinar presenter</title>
<link rel="stylesheet" href="https://fonts.googleapis.com/css2?family=Rubik:wght@300;400;500;700&family=Teko:wght@500&display=swap">
<style>
  :root {
    --page: #303030;
    --label: #8a8a8a;
    --title: #ffffff;
    --orange: #f7a11c;
    --blue: #0a72bf;
    --white: #f7f7f7;
    --suite-light: #dde4f4;
    --suite-mid: #a9b6d8;
    --suite-dark: #6f7fab;
  }
  * { margin: 0; padding: 0; box-sizing: border-box; }
  html, body { width: 717px; height: 1200px; overflow: hidden; background: var(--page); }
  body { position: relative; font-family: "Rubik", sans-serif; }

  .sheet-title {
    position: absolute; top: 38px; left: 0; width: 717px;
    text-align: center; color: var(--title);
    font: 300 20px/26px "Rubik", sans-serif; letter-spacing: 0.2px;
  }
  .sample-label {
    position: absolute; left: 48px; width: 0; height: 0;
  }
  .sample-label span {
    position: absolute; transform: translate(-50%, -50%) rotate(-90deg);
    white-space: nowrap; color: var(--label);
    font: 300 16px "Rubik", sans-serif; letter-spacing: 0.5px;
  }

  .sample {
    position: absolute; left: 102px; width: 537px; height: 302px; overflow: hidden;
    box-shadow: 0 6px 18px rgba(0,0,0,0.45);
  }
  .sample svg.shapes { position: absolute; inset: 0; width: 537px; height: 302px; }
  .suite {
    position: absolute;
    background:
      radial-gradient(ellipse 45% 30% at 55% 22%, rgba(255,255,255,0.85), transparent 70%),
      radial-gradient(ellipse 50% 22% at 52% 85%, rgba(240,244,255,0.8), transparent 75%),
      linear-gradient(180deg, var(--suite-mid) 0%, var(--suite-light) 45%, var(--suite-mid) 75%, var(--suite-dark) 100%);
  }

  .brand-name {
    position: absolute; color: var(--blue);
    font: 500 28px/1 "Rubik", sans-serif; letter-spacing: -0.5px;
    transform: translateX(-50%); white-space: nowrap;
  }
  .headline-condensed {
    position: absolute; color: #fff; white-space: nowrap;
    font: 500 38px/30px "Teko", sans-serif; letter-spacing: 0;
    text-transform: uppercase;
    transform: scaleX(0.78); transform-origin: left top;
  }
  .site-url {
    position: absolute; font: 400 7.5px/1 "Rubik", sans-serif; letter-spacing: 2px;
  }
  .headline-wide {
    position: absolute; color: #fff; text-align: center;
    font: 500 24px/25px "Rubik", sans-serif; letter-spacing: 0.3px;
  }
</style>
</head>
<body>
  <h1 class="sheet-title">VIRTUAL BACKGROUND FOR E-LEARNING<br>WEBINAR PRESENTER</h1>

  <div class="sample-label" style="top:275px"><span>SAMPLE 1</span></div>
  <div class="sample-label" style="top:646px"><span>SAMPLE 2</span></div>
  <div class="sample-label" style="top:1007px"><span>SAMPLE 3</span></div>

  <section class="sample sample-side-panel" style="top:124px">
    <div class="suite" style="left:173px;top:0;width:364px;height:302px" role="img" aria-label="Photo of a modern futuristic surgical suite with ring lights and monitors"></div>
    <svg class="shapes" viewBox="0 0 537 302" aria-hidden="true">
      <rect x="0" y="0" width="173" height="302" fill="var(--white)"/>
      <path d="M0 137 H173 L188 188 L173 240 H0 Z" fill="var(--orange)"/>
    </svg>
    <div class="brand-name" style="left:86px;top:72px">PawKenri</div>
    <div class="headline-condensed" style="left:16px;top:148px">E-Learning<br>Platform for<br>Veterinarians</div>
    <div class="site-url" style="left:24px;top:280px;color:#222">WWW.PAWKENRI.COM</div>
  </section>

  <section class="sample sample-curved-corners" style="top:485px">
    <div class="suite" style="left:0;top:0;width:537px;height:302px" role="img" aria-label="Photo of a modern futuristic surgical suite with ring lights and monitors"></div>
    <svg class="shapes" viewBox="0 0 537 302" aria-hidden="true">
      <path d="M0 0 H229 C208 66 156 112 60 112 Q22 112 0 108 Z" fill="var(--orange)"/>
      <path d="M0 0 H220 C200 60 150 106 60 107 Q22 107 0 103 Z" fill="var(--white)"/>
      <path d="M0 151 C96 145 166 180 177 302 H0 Z" fill="var(--orange)"/>
      <path d="M0 156 C90 150 158 184 170 302 H0 Z" fill="var(--blue)"/>
    </svg>
    <div class="brand-name" style="left:70px;top:60px">PawKenri</div>
    <div class="headline-condensed" style="left:16px;top:189px">E-Learning<br>Platform for<br>Veterinarians</div>
    <div class="site-url" style="left:18px;top:281px;color:#fff">WWW.PAWKENRI.COM</div>
  </section>

  <section class="sample sample-bottom-wave" style="top:846px">
    <div class="suite" style="left:0;top:0;width:537px;height:302px" role="img" aria-label="Photo of a modern futuristic surgical suite with ring lights and monitors"></div>
    <svg class="shapes" viewBox="0 0 537 302" aria-hidden="true">
      <path d="M0 188 C120 160 260 170 360 178 C440 184 500 170 537 155 V302 H0 Z" fill="var(--orange)"/>
      <path d="M0 194 C120 166 260 176 360 186 C440 191 500 178 537 166 V302 H0 Z" fill="#ffffff"/>
      <path d="M50 190 C170 172 300 190 380 194 C450 197 510 186 537 176 V302 H205 C190 258 130 214 50 190 Z" fill="var(--blue)"/>
    </svg>
    <div class="brand-name" style="left:85px;top:256px">PawKenri</div>
    <div class="headline-wide" style="left:205px;width:330px;top:245px">E-LEARNING PLATFORM<br>FOR VETERINARIANS</div>
  </section>
</body>
</html>
```